Brackenford Group Website

We have a newly established brand for a company with an existing portfolio of property. The company is corporate and professional and both owns and develops property. The website should reflect a professional and stable organisation. The website should showcase the existing properties (6), have a home page that describes the company and its activities and has a "about us" page. The website will be in Wordpress and we would like the code for all pages to be sent to us by the successful designer upon completion of the job.

sorry was called from the office on an urgent matter. To be fair on submitters, i need a couple more days to finalise reviews.

Contact Information for Business Card

Brackenford Logo on front
Black background with silver logo.

Coding

Number of Pages Required

5+ page

Colors

Designer to choose colors to be used in the design.

Requirements
Must have
• Text side of card should include
• Brackenford Property Group (as title in logo font)
• Employee Name (centered)
• Job Title (centered below name)
• Address 4 lines
• Email, mobile office phone, 3 lines
• website address (probably as footer)

```html
<!DOCTYPE html>
<html lang="en">
<head>
<meta charset="utf-8">
<title>Brackenford Property Group – Business Card</title>
<link rel="stylesheet" href="https://fonts.googleapis.com/css2?family=Cinzel:wght@400;500&family=Raleway:wght@400;500;600&display=swap">
<style>
  :root {
    --stage: #a3161c;
    --card-white: #ffffff;
    --ink: #0b0b0b;
    --brand-red: #e31b23;
    --text-light: #ffffff;
    --photo-dark: #23263a;
    --photo-mid: #6c5a48;
    --photo-warm: #d9a34a;
  }
  * { margin: 0; padding: 0; box-sizing: border-box; }
  html, body {
    width: 1200px;
    height: 900px;
    overflow: hidden;
    background: var(--stage);
  }
  .card {
    position: absolute;
    left: 100px;
    top: 165px;
    width: 1000px;
    height: 570px;
    background: var(--card-white);
    overflow: hidden;
    box-shadow: 0 18px 40px rgba(0,0,0,0.35);
  }
  .card-shapes {
    position: absolute;
    inset: 0;
    width: 1000px;
    height: 570px;
  }
  .brand {
    position: absolute;
    left: 40px;
    top: 95px;
    width: 400px;
    text-align: center;
    font-family: "Cinzel", serif;
    font-weight: 400;
    color: var(--ink);
  }
  .brand-name {
    font-size: 46px;
    letter-spacing: 3px;
    line-height: 1;
    padding-bottom: 8px;
    border-bottom: 2px solid var(--ink);
  }
  .brand-sub {
    margin-top: 8px;
    font-size: 17px;
    letter-spacing: 4px;
  }
  .person {
    position: absolute;
    left: 45px;
    top: 272px;
    color: var(--text-light);
  }
  .person-name {
    font-family: "Cinzel", serif;
    font-size: 40px;
    letter-spacing: 2px;
    line-height: 1;
    padding-bottom: 8px;
    border-bottom: 3px solid var(--brand-red);
    display: inline-block;
  }
  .person-title {
    margin-top: 10px;
    font-family: "Raleway", sans-serif;
    font-size: 17px;
    letter-spacing: 1px;
    text-transform: uppercase;
  }
  .address {
    position: absolute;
    left: 45px;
    top: 380px;
    font-family: "Raleway", sans-serif;
    font-size: 24px;
    line-height: 1.2;
    color: var(--ink);
    font-weight: 500;
  }
  .address-company {
    display: flex;
    align-items: center;
    gap: 10px;
    color: var(--brand-red);
    font-weight: 600;
  }
  .contact {
    position: absolute;
    right: 32px;
    top: 322px;
    text-align: right;
    font-family: "Raleway", sans-serif;
    font-size: 23px;
    font-weight: 500;
    color: var(--text-light);
    line-height: 1.9;
  }
  .contact-line {
    display: flex;
    justify-content: flex-end;
    align-items: center;
    gap: 12px;
    white-space: nowrap;
  }
  .website {
    position: absolute;
    left: 0;
    right: 0;
    top: 500px;
    text-align: center;
    font-family: "Raleway", sans-serif;
    font-size: 28px;
    font-weight: 500;
    letter-spacing: 7px;
    color: var(--text-light);
  }
  .website-domain { text-transform: uppercase; }
</style>
</head>
<body>
  <div class="card">
    <svg class="card-shapes" viewBox="0 0 1000 570">
      <defs>
        <linearGradient id="photo-tones" x1="0" y1="0" x2="0.6" y2="1">
          <stop offset="0" stop-color="var(--photo-dark)"/>
          <stop offset="0.55" stop-color="var(--photo-mid)"/>
          <stop offset="1" stop-color="var(--photo-warm)"/>
        </linearGradient>
      </defs>
      <polygon class="property-photo" role="img" aria-label="Night photograph of lit apartment towers and a city street in the CBD" points="470,0 1000,0 1000,300 470,300" fill="url(#photo-tones)"/>
      <polygon class="name-band" points="0,250 420,250 500,370 0,370" fill="var(--ink)"/>
      <polygon class="contact-band" points="470,300 1000,300 1000,470 600,470" fill="var(--brand-red)"/>
      <rect class="footer-band" x="0" y="470" width="1000" height="100" fill="var(--ink)"/>
    </svg>

    <div class="brand">
      <div class="brand-name">BRACKENFORD</div>
      <div class="brand-sub">PROPERTY GROUP</div>
    </div>

    <div class="person">
      <div class="person-name">JOHN DOE</div>
      <div class="person-title">Cheif Executive</div>
    </div>

    <div class="address">
      <div class="address-company">
        <svg width="16" height="22" viewBox="0 0 16 22" aria-hidden="true">
          <path d="M8 0C3.6 0 0 3.5 0 7.9 0 13.5 8 22 8 22s8-8.5 8-14.1C16 3.5 12.4 0 8 0zm0 11a3 3 0 1 1 0-6 3 3 0 0 1 0 6z" fill="var(--brand-red)"/>
        </svg>
        Brackenford Group Ltd
      </div>
      <div class="address-lines">Level 6, Harwick House 20<br>Harwick Lane Auckland CBD</div>
    </div>

    <div class="contact">
      <div class="contact-line">+64-9-415-3870
        <svg width="20" height="20" viewBox="0 0 24 24" aria-hidden="true">
          <path d="M6.6 10.8a15.1 15.1 0 0 0 6.6 6.6l2.2-2.2c.3-.3.7-.4 1-.2 1.1.4 2.3.6 3.6.6.6 0 1 .4 1 1V20c0 .6-.4 1-1 1A17 17 0 0 1 3 4c0-.6.4-1 1-1h3.5c.6 0 1 .4 1 1 0 1.3.2 2.5.6 3.6.1.3 0 .7-.2 1z" fill="var(--text-light)"/>
        </svg>
      </div>
      <div class="contact-line">jdoe@brackenfordgroup.co.nz
        <svg width="22" height="16" viewBox="0 0 24 18" aria-hidden="true">
          <rect x="0" y="0" width="24" height="18" fill="var(--text-light)"/>
          <path d="M0 0l12 9 12-9" fill="none" stroke="var(--brand-red)" stroke-width="2"/>
        </svg>
      </div>
    </div>

    <div class="website">www.<span class="website-domain">brackenfordgroup</span>.co.nz</div>
  </div>
</body>
</html>
```